●A4サイズ1ページにつき、横5列・縦6列で商品を配置し、各商品名、品番、画像、コピー、税込価格を入れてください
(商品の詳細説明やカラー、サイズなどはネットショップを見てもらうので記載不要です)

●定期的に商品の入れ替えを行うので、各商品の入れ替えがしやすいレイアウト、デザインにしてください

●商品はジャンルごとにまとめて掲載するので、その場所が何のジャンルかわかるようにしてください

●コンペで制作いただく1ページ目の商品・ジャンルと参考URLは添付ファイルをご覧ください

●ショップリニューアルを予定しており、リニューアル後のショップイメージで作成をお願いします

●1ページ目の上2段分のスペースに下記内容を入れてください
・ショップロゴ(添付ファイル:リニューアル前後で入れ替えできるようにしてください)
・注文方法(ショップURL(トップ画面右上の「search」で品番か商品名を検索)、2次元バーコード、「トルミナショップ」で検索、TEL、FAX)
・当日出荷について
・交換返品サービスについて
・送料無料クーポン(商品到着から30日以内、商品到着日記入欄、クーポンコード(K3928P)、使用方法(ご連絡欄記入、電話の場合は口頭))
A4
4ページ
重視する点・検討基準
・厳選した商品を取り扱っている信頼感と親しみやすさを感じさせるイメージ・デザイン
・各商品の特長が一目でわかり、興味を持ってもらえるような画像、コピー、デザイン
・送料無料クーポンが一目でわかり、期限内に注文しないと損をしてしまうと感じさせる見せ方
・他ショップでは行っていないサイズ交換・返品1年保証サービスの価値が伝わる見せ方

納品形式
Illustrator(CS4以下)またはPhotoshop(CS4以下)、及び確認用の高解像度JPGでお願いします。
アウトライン済/未アウトラインデータの両方お願いします。
使用されているフォントと制作環境もお知らせください。
印刷会社でそのまま印刷できるものを納品ください。
参考URLに誤りがありました。

http://tolmina-shop.com/tolmina/7.1/141/

http://tolmina-shop.com/tolmina/7.1/911/

よろしくお願いいたします。
報酬について説明不足だったかもしれません。
今回の金額は依頼内容である全4ページ分の報酬金額です。
1ページ分と伝わってしまった方には申し訳ありません。
紙面で使用する画像・文章は主にこちらを参考にしてください。
http://tolminashop.com/ranking/
これだけで不十分と思われる商品がありましたら、各商品ページから画像・文章を取ってきてください。

予想以上に作業の手間がかかるという声をいただきましたので、依頼金額を増額し、締め切りを延長させていただきました。

デザイン・レイアウトがわかりやすく、商品説明もポイントを捉えて入れていただいたご提案を選ばせていただきました。

商品点数が多く手間がかかったと思いますが、良いご提案をいただきありがとうございました。

```html
<!DOCTYPE html>
<html lang="ja">
<head>
<meta charset="utf-8">
<title>すこやかなかま 商品カタログ</title>
<link href="https://fonts.googleapis.com/css2?family=M+PLUS+Rounded+1c:wght@500;800&family=Noto+Sans+JP:wght@400;700;900&display=swap" rel="stylesheet">
<style>
:root{
  --pink:#e8508a; --pink-soft:#fbe1ec; --green:#3aa14a; --green-soft:#e4f3e1;
  --maroon:#8c1f2b; --red:#e0201c; --ink:#333; --line:#d8d8d8; --cream:#fff8fb;
}
*{box-sizing:border-box;margin:0;padding:0}
html,body{width:844px;height:1200px;overflow:hidden;background:#fff}
body{font-family:"Noto Sans JP",sans-serif;color:var(--ink);position:relative}
.header{position:absolute;left:0;top:0;width:844px;height:380px;background:linear-gradient(#fdeef4,#fff)}
.logo-box{position:absolute;left:14px;top:12px;width:490px;height:112px;background:#fff;border:2px solid var(--pink);border-radius:14px}
.logo-name{position:absolute;left:24px;top:14px;font-family:"M PLUS Rounded 1c",sans-serif;font-weight:800;font-size:46px;color:var(--green);letter-spacing:2px}
.logo-name::before{content:"";display:inline-block;width:18px;height:18px;border-radius:50%;background:var(--pink);margin-right:8px;vertical-align:middle}
.tagline{position:absolute;left:34px;top:76px;font-size:15px;color:var(--pink);font-weight:700}
.mascot{position:absolute;right:12px;top:8px;width:80px;height:94px;border-radius:40px 40px 10px 10px;background:linear-gradient(#f9c7da,#fde9f0)}
.coupon{position:absolute;left:14px;top:136px;width:300px;height:160px;background:var(--maroon);border-radius:8px;color:#fff;padding:10px 12px}
.coupon .code{background:#fff;color:var(--maroon);display:inline-block;padding:2px 10px;border-radius:4px;font-weight:900;font-size:18px}
.coupon .code small{font-size:10px;margin-right:6px}
.coupon .title{font-size:28px;font-weight:900;color:#ffe35a;margin-top:4px;letter-spacing:1px;line-height:1.3}
.coupon .limit{font-size:13px;margin-top:2px}
.coupon .limit b{color:#ffe35a;font-size:24px}
.coupon .date{margin-top:4px;background:#fff;color:var(--ink);font-size:11px;padding:3px 8px;border-radius:3px}
.badges{position:absolute;left:324px;top:136px;width:180px}
.badge{width:84px;height:84px;border-radius:50%;color:#fff;font-weight:900;text-align:center;display:inline-flex;flex-direction:column;justify-content:center;font-size:17px;line-height:1.15}
.badge.g{background:var(--green)} .badge.p{background:var(--pink);margin-left:6px}
.badge small{font-size:10px;font-weight:700}
.badge-note{font-size:11px;line-height:1.45;margin-top:8px}
.badge-note b{color:var(--red)}
.guide{position:absolute;left:516px;top:12px;width:316px;height:352px;background:#fff;border:2px solid var(--green);border-radius:10px;padding:10px 12px;font-size:11px;line-height:1.5}
.guide h2{background:var(--green);color:#fff;font-size:15px;border-radius:4px;padding:2px 10px;margin-bottom:6px}
.guide .lead{padding-right:76px}
.guide .url{color:var(--pink);font-weight:700;font-size:14px;margin:4px 0}
.code2d{position:absolute;right:12px;top:44px;width:66px;height:66px;background:#e6e6e6;border:1px solid #bbb}
.search{display:flex;margin:8px 0}
.search span{border:1px solid #999;flex:1;padding:3px 6px;font-size:12px}
.search em{font-style:normal;background:#666;color:#fff;padding:3px 10px;font-size:12px}
.contact{margin-top:10px;border-top:1px dashed var(--green);padding-top:8px;font-size:15px;font-weight:900;color:var(--green)}
.contact span{color:var(--ink);font-size:10px;font-weight:400;margin-left:4px}
.notice{position:absolute;left:14px;top:304px;width:490px;height:60px;background:#fff;border:1px solid var(--line);border-radius:6px;padding:7px 12px;font-size:11px;line-height:1.6}
.notice b{color:var(--pink)}
.grid{position:absolute;left:8px;top:385px;width:798px;display:grid;grid-template-columns:repeat(5,1fr);grid-auto-rows:201px;gap:0}
.item{border:1px solid var(--line);margin:2px;padding:5px 6px;display:flex;flex-direction:column;background:#fff}
.copy{font-size:10.5px;font-weight:900;line-height:1.35;height:44px}
.copy mark{background:none;color:var(--pink)}
.copy .g{color:var(--green)}
.photo{flex:1;border-radius:4px;background:linear-gradient(135deg,#f1ece6,#d9d3cb);margin:3px 0}
.name{font-size:9.5px;color:#555;height:14px;overflow:hidden;white-space:nowrap}
.price{display:flex;align-items:center;justify-content:space-between}
.num{background:var(--ink);color:#fff;font-size:10px;padding:1px 4px;border-radius:2px}
.yen{color:var(--red);font-weight:900;font-size:19px}
.yen small{font-size:11px}
.genre{position:absolute;left:812px;width:26px;color:#fff;font-weight:900;font-size:17px;writing-mode:vertical-rl;text-align:center;display:flex;align-items:center;justify-content:center;letter-spacing:6px;border-radius:4px}
.genre.new{top:387px;height:398px;background:var(--green)}
.genre.beauty{top:789px;height:398px;background:var(--pink)}
</style>
</head>
<body>
<header class="header">
  <div class="logo-box">
    <div class="logo-name">すこやかなかま</div>
    <div class="tagline">〜 美は健康なり、健康は美なり 〜</div>
    <div class="mascot" role="img" aria-label="ショップのマスコットイラスト"></div>
  </div>
  <div class="coupon">
    <div class="code"><small>クーポンコード</small>K3928P</div>
    <div class="title">送料無料クーポン</div>
    <div class="limit">商品到着日から <b>30</b>日以内</div>
    <div class="date">商品到着日　　　月　　　日</div>
  </div>
  <div class="badges">
    <div class="badge g"><small>平日15時まで</small>当日<br>出荷</div><div class="badge p"><small>サイズ交換</small>1年<br>保証</div>
    <p class="badge-note">平日15時までのご注文は<b>当日出荷</b>。サイズ交換・返品は<b>1年間</b>無料で承ります。</p>
  </div>
  <div class="notice">ご注文時の<b>ご連絡欄</b>にクーポンコードをご記入ください。お電話の場合は<b>口頭</b>でお伝えください。送料が無料になります。</div>
  <div class="guide">
    <h2>ご注文方法</h2>
    <div class="code2d" role="img" aria-label="ショップURLの2次元バーコード"></div>
    <p class="lead">ネットショップからのご注文はこちら</p>
    <p class="url">http://sukoyaka-nakama.jp/</p>
    <p class="lead">トップ画面右上の「search」に品番か商品名を入力して検索してください。</p>
    <div class="search"><span>すこやかなかま</span><em>検索</em></div>
    <p>ホームページからもご注文いただけます。</p>
    <p>お電話・FAXでもご注文を承っております。受付時間は平日9時〜18時です。</p>
    <div class="contact">tel. 048-512-3467<span>平日9時〜18時</span></div>
    <div class="contact">fax. 048-512-3468<span>24時間受付</span></div>
  </div>
</header>

<main class="grid">
  <div class="item"><p class="copy">ガチガチに固まった<mark>肩、背中、腰</mark>も気持ちよく伸ばす!</p><div class="photo" role="img" aria-label="ストレッチクッションの写真"></div><p class="name">ストレッチボールクッション</p><div class="price"><span class="num">545</span><span class="yen">3,780<small>円</small></span></div></div>
  <div class="item"><p class="copy">緩衝シューズで<mark>快適歩行</mark>、足裏からむくみもケア</p><div class="photo" role="img" aria-label="インソールの写真"></div><p class="name">快適ウォークインソール</p><div class="price"><span class="num">142</span><span class="yen">2,376<small>円</small></span></div></div>
  <div class="item"><p class="copy">膝裏、背中などの<span class="g">お悩み解消</span>プロサポーター</p><div class="photo" role="img" aria-label="サポーターの写真"></div><p class="name">膝用プロサポーター</p><div class="price"><span class="num">318</span><span class="yen">2,052<small>円</small></span></div></div>
  <div class="item"><p class="copy">使っている時も背筋がピーン<mark>5本指</mark>でしっかり支える</p><div class="photo" role="img" aria-label="5本指ソックスの写真"></div><p class="name">姿勢サポート5本指ソックス</p><div class="price"><span class="num">227</span><span class="yen">1,728<small>円</small></span></div></div>
  <div class="item"><p class="copy">7つの効果でスリムに<mark>オーダーメイド</mark>ではきやすい</p><div class="photo" role="img" aria-label="サンダルの写真"></div><p class="name">サンダルタイプインソール</p><div class="price"><span class="num">601</span><span class="yen">8,423<small>円</small></span></div></div>

  <div class="item"><p class="copy">ちょっとリボンで<mark>おしゃれ</mark>に腰をすっきり支える</p><div class="photo" role="img" aria-label="リボン付き骨盤ベルトの写真"></div><p class="name">リボン骨盤ベルト</p><div class="price"><span class="num">233</span><span class="yen">5,538<small>円</small></span></div></div>
  <div class="item"><p class="copy">1日5分、寝ながら<span class="g">背中をぐ〜っと</span>伸ばす</p><div class="photo" role="img" aria-label="ストレッチ器具の写真"></div><p class="name">寝ながら背伸ばしマット</p><div class="price"><span class="num">760</span><span class="yen">3,480<small>円</small></span></div></div>
  <div class="item"><p class="copy">現役ナースが開発<mark>細いゴム</mark>で手軽に脚の疲れに</p><div class="photo" role="img" aria-label="着圧ソックスの写真"></div><p class="name">ナース開発着圧ソックス</p><div class="price"><span class="num">164</span><span class="yen">6,080<small>円</small></span></div></div>
  <div class="item"><p class="copy">美しい<mark>くびれ</mark>をつくる座ってできるエクササイズ</p><div class="photo" role="img" aria-label="エクササイズクッションの写真"></div><p class="name">くびれエクササイズクッション</p><div class="price"><span class="num">319</span><span class="yen">8,477<small>円</small></span></div></div>
  <div class="item"><p class="copy">骨盤から正しく<span class="g">全身の血行促進</span>で体温アップ</p><div class="photo" role="img" aria-label="骨盤チェアの写真"></div><p class="name">骨盤サポートチェア</p><div class="price"><span class="num">880</span><span class="yen">14,580<small>円</small></span></div></div>

  <div class="item"><p class="copy">腰に優しい円座<mark>低反発</mark>でお尻を包み込む</p><div class="photo" role="img" aria-label="円座クッションの写真"></div><p class="name">低反発円座クッション</p><div class="price"><span class="num">511</span><span class="yen">5,400<small>円</small></span></div></div>
  <div class="item"><p class="copy">1日5分なら<mark>腰痛</mark>にもすらり美脚をサポート</p><div class="photo" role="img" aria-label="美脚ベルトの写真"></div><p class="name">美脚スリムベルト</p><div class="price"><span class="num">148</span><span class="yen">7,179<small>円</small></span></div></div>
  <div class="item"><p class="copy">寝ながら姿勢を整える<span class="g">高機能</span>クッション</p><div class="photo" role="img" aria-label="枕型クッションの写真"></div><p class="name">スタイルキーパー</p><div class="price"><span class="num">436</span><span class="yen">5,076<small>円</small></span></div></div>
  <div class="item"><p class="copy">膝の悩みに<mark>オーダーメイド</mark>の中敷きでしっかり</p><div class="photo" role="img" aria-label="中敷きの写真"></div><p class="name">ひざケアインソール</p><div class="price"><span class="num">117</span><span class="yen">9,334<small>円</small></span></div></div>
  <div class="item"><p class="copy">天然素材で<span class="g">肌にやさしい</span>快適パッド</p><div class="photo" role="img" aria-label="パッドの写真"></div><p class="name">ナチュラルケアパッド</p><div class="price"><span class="num">223</span><span class="yen">9,720<small>円</small></span></div></div>

  <div class="item"><p class="copy">脚を<mark>すっきり</mark>引き締めむくみを毎日ケア</p><div class="photo" role="img" aria-label="レッグケア用品の写真"></div><p class="name">すっきりレッグサポーター</p><div class="price"><span class="num">237</span><span class="yen">6,372<small>円</small></span></div></div>
  <div class="item"><p class="copy">30万人が愛用の<mark>ベストセラー</mark>ストレッチ器</p><div class="photo" role="img" aria-label="ストレッチ器具の写真"></div><p class="name">ストレッチボードプロ</p><div class="price"><span class="num">228</span><span class="yen">30,651<small>円</small></span></div></div>
  <div class="item"><p class="copy">3人の脚を支える<span class="g">高機能</span>マッサージ器</p><div class="photo" role="img" aria-label="マッサージ器の写真"></div><p class="name">フットリラックスマシン</p><div class="price"><span class="num">500</span><span class="yen">36,000<small>円</small></span></div></div>
  <div class="item"><p class="copy">正しい姿勢が<mark>美しさ</mark>をつくる骨盤チェア</p><div class="photo" role="img" aria-label="姿勢矯正チェアの写真"></div><p class="name">美姿勢チェア</p><div class="price"><span class="num">210</span><span class="yen">15,223<small>円</small></span></div></div>
  <div class="item"><p class="copy">血行を促し<span class="g">じんわり温める</span>ジャストフィット</p><div class="photo" role="img" aria-label="温熱サポーターの写真"></div><p class="name">温熱ジャストフィット</p><div class="price"><span class="num">233</span><span class="yen">13,166<small>円</small></span></div></div>
</main>

<div class="genre new">新商品</div>
<div class="genre beauty">美容</div>
</body>
</html>
```